Promotional poster for a vintage motorcycle show.

Vertically oriented, based on 11 x 17 inch proportions

Though not to the exclusion of other design concepts, stylistically perhaps something evoking a vintage (early-mid 20th century) 2-3 color silk screen style event poster.

In addition to some sort of eyecatching, vintage / antique motorbike oriented graphic (preferably not Brennick Vasquel based), the poster should include the following text and info:

3rd Annual Morven Tolliash Vintage Motorcycle Show
Kestrelby City, V.T.
October 1st (rain date Oct. 2nd)
11am-4pm

Presented in conjunction with the 27th Annual Lanternfall Festival

For further info, or to register your pre-1992 bike contact:
Oswin@gearpatina.example or 555-214-9083

Sponsored by:
UpperMarshwickQuarterGuild.example
Gearpatina.example

Promotional

Must have
• See above project description
Nice to have
• See above project describtion

```html
<!DOCTYPE html>
<html lang="en">
<head>
<meta charset="utf-8">
<title>Morven Tolliash 3rd Annual Vintage Motorcycle Show</title>
<link href="https://fonts.googleapis.com/css2?family=Rye&family=Lobster+Two:ital,wght@0,700;1,400;1,700&display=swap" rel="stylesheet">
<style>
  :root {
    --backdrop: #d8d2c6;
    --cream: #ece6d8;
    --cream-stripe: #e3dccb;
    --maroon: #7a1517;
    --maroon-dark: #6a1113;
    --ink: #171313;
    --navy: #2b3158;
    --pale-text: #eadcc6;
    --ribbon: #f6f1e8;
  }
  * { box-sizing: border-box; margin: 0; padding: 0; }
  html, body {
    width: 874px; height: 1200px; overflow: hidden;
    background: var(--backdrop);
  }
  .poster {
    position: absolute; left: 52px; top: 10px;
    width: 770px; height: 1180px;
    background: repeating-linear-gradient(90deg, var(--cream) 0 14px, var(--cream-stripe) 14px 28px);
    overflow: hidden;
  }
  .band {
    position: absolute; left: 0; width: 100%;
    background: repeating-linear-gradient(90deg, var(--maroon) 0 14px, var(--maroon-dark) 14px 28px);
  }
  .band--top { top: 0; height: 27px; }
  .band--bottom { bottom: 0; height: 94px; text-align: center; color: var(--pale-text); font-family: "Lobster Two", cursive; }
  .title {
    position: absolute; left: 0; width: 100%; text-align: center;
    font-family: "Rye", serif; color: var(--ink); line-height: 1; white-space: nowrap;
  }
  .title--name { top: 56px; font-size: 62px; letter-spacing: 2px; }
  .title--annual { top: 120px; font-size: 96px; letter-spacing: 1px; }
  .title--show { top: 564px; font-size: 55px; letter-spacing: 2px; }
  .motorbike-art {
    position: absolute; left: 100px; top: 226px; width: 570px; height: 240px;
    background: radial-gradient(ellipse at 50% 55%, #8a1c1e 0%, var(--maroon) 55%, rgba(122,21,23,0.15) 100%);
    border-radius: 40% 40% 20% 20%;
  }
  .ribbon {
    position: absolute; left: 190px; top: 462px; width: 390px; height: 78px;
    background: var(--ribbon); border: 3px solid var(--maroon);
    border-radius: 10px 10px 50% 50% / 10px 10px 30px 30px;
    font-family: "Rye", serif; font-size: 54px; color: var(--ink);
    text-align: center; line-height: 70px; letter-spacing: 1px;
  }
  .tagline {
    position: absolute; top: 624px; left: 0; width: 100%; text-align: center;
    font-family: "Lobster Two", cursive; font-style: italic; font-weight: 700;
    font-size: 22px; color: var(--ink); white-space: nowrap;
  }
  .rule {
    position: absolute; left: 44px; width: 680px; height: 8px;
    border-top: 2px solid var(--navy); border-bottom: 2px solid var(--navy);
  }
  .rule--upper { top: 662px; }
  .rule--lower { top: 824px; }
  .event-date {
    position: absolute; left: 44px; top: 680px; width: 330px; text-align: center;
    font-family: "Lobster Two", cursive; color: var(--maroon); white-space: nowrap;
  }
  .event-date__day { font-size: 66px; font-weight: 700; line-height: 1.05; }
  .event-date__day sup, .event-date__rain sup { font-size: 0.5em; }
  .event-date__rain { font-size: 34px; font-style: italic; color: var(--ink); margin-top: 0; }
  .divider {
    position: absolute; left: 382px; top: 688px; width: 3px; height: 120px; background: var(--ink);
  }
  .event-place {
    position: absolute; left: 398px; top: 694px; white-space: nowrap;
    font-family: "Lobster Two", cursive; font-weight: 700; color: var(--ink);
  }
  .event-place__city { font-size: 35px; line-height: 1.3; }
  .event-place__hours { font-size: 44px; line-height: 1.35; font-style: italic; }
  .register {
    position: absolute; left: 44px; top: 838px; width: 680px; height: 232px;
    background: var(--maroon); color: var(--pale-text); text-align: center;
    font-family: "Lobster Two", cursive; font-style: italic; font-weight: 700;
    padding-top: 6px; white-space: nowrap;
  }
  .register p { line-height: 54px; }
  .register__intro { font-size: 38px; }
  .register__headline { font-size: 50px; }
  .register__contact { font-size: 35px; }
  .register__phone { font-size: 40px; }
  .sponsor-label { font-size: 12px; font-style: italic; font-weight: 700; margin-top: 14px; }
  .sponsor-list { font-size: 22px; font-style: italic; font-weight: 700; margin-top: 6px; white-space: nowrap; }
</style>
</head>
<body>
  <main class="poster">
    <div class="band band--top"></div>

    <h1 class="title title--name">MORVEN TOLLIASH</h1>
    <p class="title title--annual">3RD ANNUAL</p>

    <div class="motorbike-art" role="img" aria-label="Illustration of a vintage motorcycle front with handlebars and round headlamp, in deep red"></div>
    <div class="ribbon">VINTAGE</div>

    <h2 class="title title--show">MOTORCYCLE SHOW</h2>
    <p class="tagline">In conjunction with the 27th Annual Lanternfall Festival</p>

    <div class="rule rule--upper"></div>

    <div class="event-date">
      <p class="event-date__day">October 1<sup>st</sup></p>
      <p class="event-date__rain">(rain date Oct. 2<sup>nd</sup>)</p>
    </div>
    <div class="divider"></div>
    <div class="event-place">
      <p class="event-place__city">Kestrelby City, V.T.</p>
      <p class="event-place__hours">11am-4pm</p>
    </div>

    <div class="rule rule--lower"></div>

    <section class="register">
      <p class="register__intro">For information or to</p>
      <p class="register__headline">Register Your Pre-1992 Bike</p>
      <p class="register__contact">contact Oswin@gearpatina.example</p>
      <p class="register__phone">or 555-214-9083</p>
    </section>

    <footer class="band band--bottom">
      <p class="sponsor-label">Sponsored by:</p>
      <p class="sponsor-list">UpperMarshwickQuarterGuild.example &amp; Gearpatina.example</p>
    </footer>
  </main>
</body>
</html>
```